Tambrel Couriers Web design

Take a look at our existing website(www.tmbrl-example.com) and design a new one, plus coding and recreate an existing logo.

```html
<!DOCTYPE html>
<html lang="en">
<head>
<meta charset="utf-8">
<title>Tambrel Couriers</title>
<link href="https://fonts.googleapis.com/css2?family=Poppins:ital,wght@0,300;0,400;0,500;0,700;0,800;1,300&display=swap" rel="stylesheet">
<style>
:root{
  --orange:#f7931e;
  --dark:#363a3f;
  --footer:#333333;
  --text:#666a70;
  --heading:#3a3a3a;
  --light:#f6f7f9;
  --white:#ffffff;
}
*{box-sizing:border-box;margin:0;padding:0}
html,body{width:1200px;height:4060px;overflow:hidden}
body{font-family:'Poppins',sans-serif;color:var(--text);background:var(--white);position:relative}
.abs{position:absolute}
a{color:inherit;text-decoration:none}

/* nav */
.nav{left:0;top:0;width:1200px;height:49px;background:var(--dark);display:flex;align-items:center;justify-content:space-between;padding:0 166px}
.brand{color:var(--white);font-weight:700;font-size:17px;letter-spacing:.5px;display:flex;align-items:center;gap:8px}
.brand-dot{width:12px;height:12px;background:var(--orange)}
.menu{display:flex;gap:19px;font-size:11px;letter-spacing:.6px;color:var(--white);font-weight:400}
.menu .active{color:var(--orange)}

/* hero */
.hero{left:0;top:49px;width:1200px;height:501px;background:linear-gradient(120deg,#6a5a4a 0%,#8f7358 35%,#b08b62 60%,#7d6a58 100%)}
.hero-title{left:0;top:140px;width:1200px;text-align:center;color:var(--white);font-weight:800;font-size:52px;line-height:61px;letter-spacing:.5px}
.btn{display:flex;align-items:center;justify-content:center;background:var(--orange);color:var(--white);font-size:12px;letter-spacing:2.5px;font-weight:500}
.hero-btn{left:505px;top:355px;width:190px;height:44px}

/* features */
.features{left:166px;top:471px;width:867px;height:303px;display:flex;box-shadow:0 6px 14px rgba(0,0,0,.25)}
.feature{flex:1;background:var(--orange);color:var(--white);text-align:center;padding-top:26px}
.feature .ring{width:62px;height:62px;border:2px solid rgba(255,255,255,.8);border-radius:50%;margin:0 auto;display:flex;align-items:center;justify-content:center}
.feature h3{font-weight:400;font-size:17px;margin-top:22px}
.feature p{font-size:11.5px;line-height:19px;margin:20px auto 0;width:200px;opacity:.85;font-weight:300}
.quote{flex:1;background:var(--dark);color:var(--white);padding:40px 38px 0}
.quote h3{text-align:center;font-weight:400;font-size:16px;margin-bottom:20px}
.quote label{display:block;font-size:11px;margin-bottom:7px;font-weight:300}
.quote .field{height:30px;border:1px solid #c9c9c9;font-size:10px;font-style:italic;color:#bbb;padding:8px 10px;margin-bottom:16px;font-weight:300}
.quote .btn{height:32px}

/* section headings */
.sec-title{left:0;width:1200px;text-align:center;color:var(--orange);font-weight:700;font-size:24px}
.sec-sub{left:0;width:1200px;text-align:center;font-size:12px;font-weight:300}
.rule{left:568px;width:64px;height:2px;background:var(--orange)}

/* service columns */
.cols{left:166px;width:870px;display:flex;gap:0}
.item{display:flex;gap:18px}
.item svg{flex:none}
.item h4{font-weight:400;font-size:15.5px;color:var(--heading);margin-bottom:9px}
.item p{font-size:12.2px;line-height:21.3px;font-weight:300}
.item .more{color:var(--orange);font-size:12px;margin-top:16px;display:block;font-weight:300}

/* carousel */
.tiles{left:0;top:1397px;width:1200px;height:342px;display:flex}
.tile{flex:1;position:relative}
.tile span{position:absolute;bottom:34px;left:0;width:100%;text-align:center;color:var(--white);font-size:18.5px;font-weight:400}
.arrows{left:560px;top:1762px;display:flex;gap:32px}

/* more services */
.more-bg{left:0;top:1805px;width:1200px;height:641px;background:var(--light)}

/* video */
.video{left:0;top:2446px;width:1200px;height:468px;background:linear-gradient(180deg,#4a4c50 0%,#6b6d70 45%,#3e4044 100%)}
.video-text{left:0;top:2668px;width:1200px;text-align:center;color:var(--white);font-size:33px;line-height:38px;font-weight:300}
.video-brand{left:745px;top:2790px;color:rgba(255,255,255,.55);font-size:34px;font-weight:700;letter-spacing:1px}

/* testimonial */
.avatar{left:562px;top:3052px;width:76px;height:76px;border-radius:50%;background:linear-gradient(160deg,#bfe3e8,#2d3a3c)}
.t-name{left:0;top:3146px;width:1200px;text-align:center;font-size:13px}
.t-quote{left:300px;top:3187px;width:600px;text-align:center;font-size:12.5px;font-style:italic;line-height:21px;font-weight:300}
.t-arrow{width:38px;height:38px;border-radius:50%;background:#d7d7d7;display:flex;align-items:center;justify-content:center;top:3135px}
.divider{left:0;top:3323px;width:1200px;height:1px;background:#e4e4e4}
.try{left:0;top:3380px;width:1200px;text-align:center;font-size:25px;color:var(--heading)}
.try-btn{left:508px;top:3454px;width:184px;height:44px}

/* footer */
.footer{left:0;top:3562px;width:1200px;height:498px;background:var(--footer)}
.f-col{top:3662px;color:#aaa;font-size:12px}
.f-col h5{color:var(--white);font-size:12px;font-weight:400;margin-bottom:20px}
.f-col li{list-style:none;margin-bottom:12px;font-weight:300}
.social{display:flex;gap:26px}
.social i{display:block;width:9px;height:9px;border-radius:50%;background:#aaa}
.sub{display:flex}
.sub .in{width:136px;height:32px;border:1px solid #666;font-size:11px;color:#999;padding:8px 10px;font-weight:300}
.sub .btn{width:63px;height:32px;letter-spacing:2px}
.f-line{left:166px;top:3892px;width:867px;height:1px;background:#474747}
.copy{left:0;top:3934px;width:1200px;text-align:center;font-size:12px;color:#888;font-weight:300}
</style>
</head>
<body>

<header class="abs nav">
  <div class="brand"><span class="brand-dot"></span>TAMBREL</div>
  <nav class="menu">
    <a class="active">HOME</a><a>ABOUT US</a><a>SERVICES ⌄</a><a>RATES</a><a>CUSTOMER BENEFITS</a><a>CONTACT</a>
  </nav>
</header>

<section class="abs hero" role="img" aria-label="Photo of a courier handing over a cardboard parcel"></section>
<h1 class="abs hero-title">WELCOME TO<br>TAMBREL<br>COURIERS</h1>
<a class="abs btn hero-btn">GET STARTED!</a>

<section class="abs features">
  <div class="feature">
    <div class="ring"><span style="font-size:28px;font-weight:500">$</span></div>
    <h3>BEST PRICES</h3>
    <p>Lorem ipsum dolor sit amet consectetur adipisicing elit. Perspiciatis ipsum odio minima tempora animi iure.</p>
  </div>
  <div class="quote">
    <h3>GET FREE QUOTE</h3>
    <label>Name</label><div class="field">Enter Name</div>
    <label>Email</label><div class="field">Enter Email</div>
    <a class="btn">GET QUOTE</a>
  </div>
  <div class="feature">
    <div class="ring"><svg width="24" height="24" viewBox="0 0 24 24"><path fill="#fff" d="M6.6 10.8a15 15 0 006.6 6.6l2.2-2.2a1 1 0 011-.25 11.4 11.4 0 003.6.57 1 1 0 011 1V20a1 1 0 01-1 1A17 17 0 013 4a1 1 0 011-1h3.5a1 1 0 011 1c0 1.25.2 2.45.57 3.57a1 1 0 01-.25 1z"/></svg></div>
    <h3>24/7 SUPPORT</h3>
    <p>Lorem ipsum dolor sit amet consectetur adipisicing elit. Perspiciatis ipsum odio minima tempora animi iure.</p>
  </div>
</section>

<h2 class="abs sec-title" style="top:834px">WHAT WE OFFER</h2>
<p class="abs sec-sub" style="top:868px">Lorem ipsum dolor sit amet.</p>
<div class="abs rule" style="top:897px"></div>

<section class="abs cols" style="top:936px">
  <div class="item" style="width:296px">
    <svg width="42" height="40" viewBox="0 0 42 40"><rect x="12" y="2" width="6" height="16" fill="#f7931e"/><rect x="7" y="7" width="16" height="6" fill="#f7931e"/><path d="M2 28c6-5 12-5 18-2h10c3 0 3 4 0 4H20M2 36c8 0 16 1 24-2l12-8" fill="none" stroke="#f7931e" stroke-width="3"/></svg>
    <div style="width:212px"><h4>Medical Delivery</h4><p>Tambrel Couriers provide a full menu of medical services that includes picking up and skillfully managing critical materials such as lab specimens, controlled substances, medications, temperature sensitive and controlled items, blood or any other medically related item that requires special handling that needs same-day delivery.</p><a class="more">Learn More</a></div>
  </div>
  <div class="item" style="width:300px">
    <svg width="40" height="36" viewBox="0 0 40 36"><path d="M3 3v30h34" fill="none" stroke="#f7931e" stroke-width="3.5"/><path d="M9 24l9-9 6 6 11-11" fill="none" stroke="#f7931e" stroke-width="3.5"/><path d="M28 8h8v8" fill="none" stroke="#f7931e" stroke-width="3.5"/></svg>
    <div style="width:220px"><h4>Banking &amp; Brokerage</h4><p>Lorem ipsum dolor sit amet consectetur adipisicing elit. Perferendis quis molestiae vitae eligendi at. Lorem ipsum dolor sit amet consectetur adipisicing elit. Saepe a assumenda aspernatur nemo libero minus deserunt iusto esse consectetur soluta eum culpa doloremque explicabo illum praesentium, quam necessitatibus ipsam fugiat?</p><a class="more">Learn More</a></div>
  </div>
  <div class="item" style="width:274px">
    <svg width="46" height="38" viewBox="0 0 46 38"><path d="M23 2v32M12 34h22M6 8h34" stroke="#f7931e" stroke-width="3" fill="none"/><path d="M2 22l5-13 5 13zM34 22l5-13 5 13z" fill="none" stroke="#f7931e" stroke-width="2.5"/><path d="M1 22h12a6 6 0 01-12 0zM33 22h12a6 6 0 01-12 0z" fill="#f7931e"/></svg>
    <div style="width:210px"><h4>Legal Filings</h4><p>Tambrel legal courier services' main attention is on meeting the needs of the legal community. Our knowledge of the Courts, the Judges, the Counties makes us very effective in what we do. We provide legal courier services that include court filings, obtaining a judge's signature, securing an immediate court date as well as subpoena deliveries etc. All these are done in a timely manner.</p><a class="more">Learn More</a></div>
  </div>
</section>

<section class="abs tiles">
  <div class="tile" role="img" aria-label="Photo of a tablet showing a delivery tracking app" style="background:linear-gradient(135deg,#c4b8b2,#e8e2df 45%,#6f6a6d)"><span>On Demand</span></div>
  <div class="tile" role="img" aria-label="Photo of an alarm clock beside parcels" style="background:linear-gradient(135deg,#b48a5e,#d6ae82 50%,#c9a0b4)"><span>Rush</span></div>
  <div class="tile" role="img" aria-label="Photo of a courier signing for a delivery" style="background:linear-gradient(135deg,#3c4a5a,#8a8f94 50%,#b98e66)"><span>Regular Service</span></div>
  <div class="tile" role="img" aria-label="Photo of city traffic light trails at night" style="background:linear-gradient(160deg,#2a3346,#7a5a3a 55%,#e0a65a)"><span>After Hours Delivery</span></div>
</section>
<div class="abs arrows">
  <svg width="20" height="16" viewBox="0 0 20 16"><path d="M19 8H2M8 2L2 8l6 6" fill="none" stroke="#222" stroke-width="2"/></svg>
  <svg width="20" height="16" viewBox="0 0 20 16"><path d="M1 8h17M12 2l6 6-6 6" fill="none" stroke="#222" stroke-width="2"/></svg>
</div>

<div class="abs more-bg"></div>
<h2 class="abs sec-title" style="top:1863px">MORE SERVICES</h2>
<p class="abs sec-sub" style="top:1902px">We Offer The Following Services</p>
<div class="abs rule" style="top:1930px"></div>

<section class="abs cols" style="top:1969px">
  <div class="item" style="width:296px">
    <svg width="42" height="38" viewBox="0 0 42 38"><path d="M1 3h7l6 22h22l4-16H11" fill="none" stroke="#f7931e" stroke-width="4"/><circle cx="16" cy="33" r="3.5" fill="#f7931e"/><circle cx="33" cy="33" r="3.5" fill="#f7931e"/></svg>
    <div style="width:212px"><h4>On-Demand</h4><p>Tambrel offers an immediate pick up and delivery of your time-sensitive documents and goods, 24 hours a day, 7 days a week via autos, station wagons and vans.</p><a class="more">Learn More</a></div>
  </div>
  <div class="item" style="width:298px">
    <svg width="42" height="34" viewBox="0 0 42 34"><path d="M21 2a19 19 0 00-19 19c0 4 1 8 3 11h32c2-3 3-7 3-11A19 19 0 0021 2z" fill="#f7931e"/><path d="M21 22l8-10" stroke="#fff" stroke-width="3"/><circle cx="21" cy="22" r="3" fill="#fff"/><circle cx="10" cy="18" r="2" fill="#fff"/><circle cx="14" cy="10" r="2" fill="#fff"/><circle cx="32" cy="18" r="2" fill="#fff"/></svg>
    <div style="width:210px"><h4>Rush</h4><p>Pick up and delivery made within 50 minutes of your call, locally. Add 1 hour for every 50 miles out of town. Available 24 hours a day, 7 days a week.</p><a class="more">Learn More</a></div>
  </div>
  <div class="item" style="width:276px">
    <svg width="30" height="40" viewBox="0 0 30 40"><rect x="1" y="5" width="28" height="34" rx="3" fill="#f7931e"/><rect x="9" y="1" width="12" height="8" rx="2" fill="#f7931e" stroke="#f6f7f9" stroke-width="2"/><path d="M7 23l6 6 11-12" fill="none" stroke="#fff" stroke-width="3.5"/></svg>
    <div style="width:222px"><h4>Regular Service</h4><p>Pick up and delivery made within 3 hours of your call, locally. Add 1 hour for every 50 miles out of town. Available Monday through Friday.</p><a class="more">Learn More</a></div>
  </div>
</section>

<section class="abs cols" style="top:2165px">
  <div class="item" style="width:296px">
    <svg width="34" height="38" viewBox="0 0 34 38"><path d="M22 2A17 17 0 1032 30 15 15 0 0122 2z" fill="#f7931e"/></svg>
    <div style="width:220px"><h4>After Hours Delivery</h4><p>Available between 6pm and 8am</p><a class="more">Learn More</a></div>
  </div>
  <div class="item" style="width:298px">
    <svg width="34" height="38" viewBox="0 0 34 38"><rect x="1" y="5" width="32" height="32" rx="3" fill="#f7931e"/><rect x="7" y="1" width="4" height="8" fill="#f7931e"/><rect x="23" y="1" width="4" height="8" fill="#f7931e"/><rect x="1" y="12" width="32" height="2" fill="#f6f7f9"/><rect x="8" y="19" width="6" height="6" fill="#fff"/></svg>
    <div style="width:216px"><h4>Same Day Service</h4><p>Call by noon, pick up and delivered by 5pm. This applies only to Harrowgate and its suburbs.</p><a class="more">Learn More</a></div>
  </div>
  <div class="item" style="width:276px">
    <svg width="46" height="36" viewBox="0 0 46 36"><rect x="1" y="4" width="28" height="22" fill="#f7931e"/><path d="M29 10h9l7 8v8H29z" fill="#f7931e"/><circle cx="10" cy="29" r="5" fill="#f7931e" stroke="#f6f7f9" stroke-width="2"/><circle cx="36" cy="29" r="5" fill="#f7931e" stroke="#f6f7f9" stroke-width="2"/><path d="M6 11h12M4 16h12" stroke="#fff" stroke-width="2"/></svg>
    <div style="width:206px"><h4>Warehousing and Distribution</h4><p>Tambrel maintains and manage a warehouse for product storage and distribution of your inventory. Large or Small, Permanent or Temporary.</p><a class="more">Learn More</a></div>
  </div>
</section>

<section class="abs video" role="img" aria-label="Photo of a delivery truck inside a loading warehouse"></section>
<svg class="abs" style="left:564px;top:2575px" width="72" height="72" viewBox="0 0 72 72"><circle cx="36" cy="36" r="34" fill="rgba(255,255,255,.15)" stroke="#fff" stroke-width="2"/><path d="M28 22l24 14-24 14z" fill="#fff"/></svg>
<p class="abs video-text">View Our Services By Watching<br>This Short Video</p>
<div class="abs video-brand">TAMBREL</div>

<h2 class="abs sec-title" style="top:2975px">WHAT PEOPLE ARE SAYING?</h2>
<div class="abs rule" style="top:3012px"></div>
<div class="abs avatar" role="img" aria-label="Portrait photo of a customer"></div>
<p class="abs t-name">Marcus, Brightline Labs (Shipping)</p>
<p class="abs t-quote">"Tambrel always pick-up and delivers on time. We've never had any problems. Who can ask for anything more?"</p>
<div class="abs t-arrow" style="left:175px"><svg width="8" height="10" viewBox="0 0 8 10"><path d="M6 1L2 5l4 4" fill="none" stroke="#fff" stroke-width="1.5"/></svg></div>
<div class="abs t-arrow" style="left:987px"><svg width="8" height="10" viewBox="0 0 8 10"><path d="M2 1l4 4-4 4" fill="none" stroke="#fff" stroke-width="1.5"/></svg></div>

<div class="abs divider"></div>
<h2 class="abs try" style="font-weight:400">Try Our Services</h2>
<a class="abs btn try-btn">GET STARTED</a>

<footer class="abs footer"></footer>
<div class="abs f-col" style="left:166px"><h5>Quick Links</h5><ul><li>About Us</li><li>Services</li><li>Testimonials</li><li>Contact Us</li></ul></div>
<div class="abs f-col" style="left:333px"><h5>Products</h5><ul><li>About Us</li><li>Services</li><li>Testimonials</li><li>Contact Us</li></ul></div>
<div class="abs f-col" style="left:500px"><h5>Features</h5><ul><li>About Us</li><li>Services</li><li>Testimonials</li><li>Contact Us</li></ul></div>
<div class="abs f-col" style="left:667px"><h5>Follow Us</h5><div class="social" style="padding-top:4px"><i></i><i></i><i></i><i></i></div></div>
<div class="abs f-col" style="left:834px"><h5>Subscribe Newsletter</h5><div class="sub"><div class="in">Enter Email</div><a class="btn">SEND</a></div></div>
<div class="abs f-line"></div>
<p class="abs copy">Copyright ©2021 All rights reserved</p>

</body>
</html>
```